Leonard Vasto Card

My father, Leonard Vasto, just retired at 69 years old and he needs a new business/social card that looks professional and includes some sort of logo - perhaps his initials LV. It needs to include his phone number and email address and that's it. So fairly limited text but still elegant.

Industry/Entity Type

Business

```html
<!DOCTYPE html>
<html lang="en">
<head>
<meta charset="utf-8">
<title>Leonard Vasto Card</title>
<link rel="stylesheet" href="https://fonts.googleapis.com/css2?family=Crimson+Text:wght@400&display=swap">
<style>
  :root {
    --backdrop: #aab3b4;
    --card-white: #ffffff;
    --card-blue: #1482c4;
    --plate-grey: #959595;
    --ink-light: #ffffff;
    --edge-shadow: rgba(40, 50, 55, 0.28);
  }
  * { box-sizing: border-box; margin: 0; padding: 0; }
  html, body {
    width: 1200px;
    height: 1000px;
    overflow: hidden;
  }
  body {
    background: var(--backdrop);
    font-family: "Crimson Text", Georgia, serif;
    position: relative;
  }
  .business-card {
    position: absolute;
    left: 150px;
    top: 240px;
    width: 900px;
    height: 520px;
    background: var(--card-white);
    box-shadow: 0 18px 40px var(--edge-shadow);
    overflow: hidden;
  }
  .card-band {
    position: absolute;
    left: 0;
    right: 0;
    top: 230px;
    bottom: 0;
    background: var(--card-blue);
  }
  .name-plate {
    position: absolute;
    left: 330px;
    top: 90px;
    width: 240px;
    height: 240px;
    background: var(--plate-grey);
    box-shadow: 0 6px 14px rgba(0, 0, 0, 0.22);
    display: flex;
    align-items: center;
    justify-content: center;
    text-align: center;
  }
  .name-plate__name {
    color: var(--ink-light);
    font-size: 34px;
    font-weight: 400;
    line-height: 1.15;
    letter-spacing: 0.04em;
    text-transform: uppercase;
  }
  .contact-line {
    position: absolute;
    left: 60px;
    top: 372px;
    display: flex;
    align-items: center;
    gap: 14px;
    color: var(--ink-light);
    font-size: 34px;
    white-space: nowrap;
  }
  .contact-line__icon {
    width: 28px;
    height: 28px;
    flex: none;
  }
  .contact-line__phone { margin-right: 36px; }
</style>
</head>
<body>
  <main class="business-card">
    <div class="card-band"></div>

    <div class="name-plate">
      <p class="name-plate__name">Leonard<br>Vasto</p>
    </div>

    <div class="contact-line">
      <svg class="contact-line__icon" viewBox="0 0 28 28" aria-hidden="true">
        <circle cx="14" cy="14" r="12.5" fill="none" stroke="#ffffff" stroke-width="1.5"/>
        <path d="M10 8.5c1-.6 1.7-.4 2.2.5l1 2c.3.7.1 1.3-.5 1.7l-.7.5c.6 1.6 1.6 2.8 3 3.6l.6-.6c.5-.5 1.2-.6 1.8-.2l1.8 1.2c.8.5.9 1.3.3 2.1-.8 1.1-2.2 1.5-3.6.9-3.3-1.5-5.6-4.1-6.6-7.4-.4-1.7.1-3.4.7-4.3z" fill="#ffffff"/>
      </svg>
      <span class="contact-line__phone">0198 765432</span>
      <span class="contact-line__email">email: leonardvasto@vastomail.com</span>
    </div>
  </main>
</body>
</html>
```